Recruitment of Brackwell Staffing for the UK market

I want a website for the UK market to attract businesses and companies to come to us for Philipine labour. We want an information site that gives all information on what we do and how we can recruit Philippine labour.
This is a recruitment site for companies to contact us with their requirements for skilled workers coming from the Philipines over to the UK to work.

Target Market(s)

Uk Companies and businesses who want Philipine skilled workers

Industry/Entity Type

REcruitment

Coding

Coded - Design and coding required

Number of Pages Required

5+ page

Font styles to use
Sans Serif

Colors
0054AA
0677BA
7BADD7
CADEEF
E8F1F8
0094D4
00A9DD
6FCCEA
C7EBF8
E9F6FB
EE7325
F08F49
F5BC92
FAE3D3
FDF4ED
EB3D1F
EC4F4E
F09395
F8D3D4
FCEDEE

Requirements
Must have
• Look professional and corperate with drop down menus for Home ,about, services,articles. training , contact us
Nice to have
• Look at Tolvery recruitment- https://tolveryrecruitment.example.co.uk/. This is my current site - https://www.brackwellstaffing.example.com/
Should not have
• Cartoons or silly pictures , needs to be corperate looking

```html
<!DOCTYPE html>
<html lang="en">
<head>
<meta charset="utf-8">
<title>Brackwell Staffing – Skilled Philippine Workers for UK Companies</title>
<link rel="stylesheet" href="https://fonts.googleapis.com/css2?family=Poppins:wght@400;500;600;700&display=swap">
<style>
:root{
  --brand:#8b3129;
  --ink:#2b2b2b;
  --white:#ffffff;
  --map-sea:#8ab4f8;
  --tone-office:#c3c6c9;
  --tone-wood:#cdbfb0;
  --tone-dark:#55595d;
  --tone-skin:#c9a48e;
}
*{margin:0;padding:0;box-sizing:border-box}
html,body{width:1200px;height:4222px;overflow:hidden;background:var(--white)}
body{position:relative;font-family:'Poppins',sans-serif;color:var(--ink)}
.photo{position:absolute}
.office{background:linear-gradient(180deg,#e3e5e7 0%,#c3c6c9 100%)}
.office-warm{background:linear-gradient(180deg,#e6e3df 0%,#b9b3ab 100%)}
.dark-desk{background:linear-gradient(180deg,#8e9195 0%,#55595d 100%)}
.hands{background:linear-gradient(180deg,#e4d8cf 0%,#c9a48e 100%)}
.factory{background:linear-gradient(180deg,#d9dadb 0%,#c7c48a 100%)}

.site-header{position:absolute;left:0;top:0;width:1200px;height:618px;box-shadow:0 6px 10px rgba(0,0,0,.15)}
.header-red{position:absolute;left:510px;top:0;width:690px;height:618px;background:var(--brand)}
.brand-name{position:absolute;left:113px;top:22px;font-size:34px;font-weight:700;color:var(--brand);display:flex;align-items:center;gap:12px}
.brand-name i{display:block;width:22px;height:22px;background:var(--brand)}
.main-nav{position:absolute;left:537px;top:34px}
.main-nav a{color:var(--white);text-decoration:none;font-size:15px;position:absolute;white-space:nowrap}
.hero-photo{left:111px;top:87px;width:979px;height:456px;background:linear-gradient(90deg,#cdbfb0 0%,#ddd2c6 50%,#f1f1f0 53%,#e2e2e2 100%)}
.hero-title{position:absolute;left:111px;top:158px;font-size:53px;font-weight:700;line-height:77px;color:var(--brand)}

.h2{position:absolute;font-size:35px;font-weight:700;color:var(--brand);white-space:nowrap}
.copy{position:absolute;font-size:16px;line-height:25.8px;color:var(--ink)}
.btn{position:absolute;height:42px;padding:0 15px;border:2px solid var(--brand);color:var(--brand);font-size:19px;font-weight:600;display:flex;align-items:center;background:var(--white)}
.panel{position:absolute;background:var(--brand);color:var(--white)}
.panel .h2,.panel .copy{color:var(--white)}
.btn.light{border-color:var(--white);color:var(--white);background:transparent}

.map{left:0;top:3350px;width:1200px;height:548px;background:linear-gradient(180deg,#8fb8f8 0%,#86b0f4 100%)}
.form-panel{left:669px;top:3383px;width:421px;height:485px}
.form-panel h3{position:absolute;left:42px;top:17px;font-size:21px;font-weight:700}
.field-label{position:absolute;left:44px;font-size:12px}
.field{position:absolute;left:44px;width:333px;height:40px;border:1px solid var(--white)}
.send{position:absolute;left:44px;top:420px;width:152px;height:38px;background:var(--white);color:var(--brand);font-size:15px;font-weight:600;display:flex;align-items:center;justify-content:center}

.site-footer{position:absolute;left:0;top:3898px;width:1200px;height:324px;background:var(--brand);color:var(--white)}
.footer-title{position:absolute;width:1200px;top:31px;text-align:center;font-size:21px;font-weight:600}
.contact-row{position:absolute;top:80px;width:1200px;display:flex;justify-content:center;gap:22px;font-size:15px;align-items:center}
.contact-row span{display:flex;align-items:center;gap:7px}
.footer-nav{position:absolute;top:125px;width:1200px;text-align:center;font-size:15px}
.social{position:absolute;top:177px;left:462px;display:flex;gap:17px}
.social span{width:56px;height:56px;border-radius:50%;background:var(--white)}
.rule{position:absolute;left:0;top:262px;width:1200px;height:1px;background:rgba(255,255,255,.6)}
.copyright{position:absolute;top:288px;width:1200px;text-align:center;font-size:15px}
</style>
</head>
<body>

<header class="site-header">
  <div class="header-red"></div>
  <div class="brand-name"><i></i>Brackwell Staffing</div>
  <nav class="main-nav">
    <a style="left:0">Home</a>
    <a style="left:75px">About</a>
    <a style="left:150px">Services</a>
    <a style="left:243px">Articles</a>
    <a style="left:329px">Training</a>
    <a style="left:420px">Contact us</a>
    <svg style="position:absolute;left:529px;top:4px" width="18" height="18" viewBox="0 0 18 18" fill="none" stroke="#fff" stroke-width="1.6"><circle cx="7.5" cy="7.5" r="5.5"/><line x1="11.5" y1="11.5" x2="16" y2="16"/></svg>
  </nav>
  <div class="photo hero-photo" role="img" aria-label="Photo: business handshake across an office desk with laptop and documents"></div>
  <h1 class="hero-title">Recruiting and<br>Placing Skilled<br>Philippine Workers<br>into UK Companies</h1>
</header>

<section>
  <div class="photo office" style="left:128px;top:712px;width:300px;height:300px" role="img" aria-label="Photo: colleagues shaking hands in a bright office"></div>
  <h2 class="h2" style="left:481px;top:730px">What the Business is About</h2>
  <p class="copy" style="left:489px;top:793px;width:490px">We source skilled workers directly from the Philippines to work in the UK. With offices , training locations and specialist recruiters we can find the highest quality individuals to add value and resources to any UK buisness. We delivery quality based on vast experience over a number of years.</p>
  <div class="btn" style="left:490px;top:948px">Read More</div>
  <div class="photo office-warm" style="left:128px;top:1031px;width:300px;height:300px" role="img" aria-label="Photo: candidates waiting on chairs for interviews"></div>
  <div class="photo factory" style="left:453px;top:1031px;width:300px;height:300px" role="img" aria-label="Photo: workers in hi-vis vests and hard hats in a factory"></div>
  <div class="photo dark-desk" style="left:772px;top:1031px;width:300px;height:300px" role="img" aria-label="Photo: hands reviewing CV documents on a desk"></div>
</section>

<section>
  <div class="photo hands" style="left:113px;top:1403px;width:358px;height:379px" role="img" aria-label="Photo: stacked hands showing teamwork"></div>
  <h2 class="h2" style="left:536px;top:1434px">What We Do</h2>
  <p class="copy" style="left:536px;top:1496px;width:470px">Our company has been estabilished in the Philippines for over 20 years. We have mainly been recruiting philippine workers for the off shore industry in asia but since brexit and the new rules on skilled workers entering the UK we have been working with UK companies who now have chance to recruit some of the finest hard working talent from the Philippines for their companies..</p>
  <div class="btn" style="left:536px;top:1704px">Read More</div>
</section>

<section>
  <div class="photo office" style="left:728px;top:1862px;width:359px;height:379px" role="img" aria-label="Photo: two professionals shaking hands at a desk"></div>
  <div class="panel" style="left:113px;top:1878px;width:687px;height:348px">
    <h2 class="h2" style="left:55px;top:29px">How We Help</h2>
    <p class="copy" style="left:58px;top:89px;width:480px">We work with companies to find skilled workers that meet the UK requirements for Visas and work permits. We guide you through the whole process and deliver highly trained people that add value to your business. We are here to help both the companies and the Philippino people to gain a better standard of living for their families.</p>
    <div class="btn light" style="left:57px;top:275px;height:40px">Read More</div>
  </div>
</section>

<section>
  <div class="photo dark-desk" style="left:113px;top:2313px;width:358px;height:380px" role="img" aria-label="Photo: hand selecting a figure from a network of people figures"></div>
  <h2 class="h2" style="left:536px;top:2345px">Where To Start</h2>
  <p class="copy" style="left:536px;top:2407px;width:480px">We need to know what your issues are and how we can understand the personnal you require , over what time frame and the number of employees you need. Once this is estabilished we start sourcing workers in the Philippines that meet your criteria while starting the process in the UK to be able to have all the documents in place to deliver your company hard working skilled individuals.</p>
  <div class="btn" style="left:536px;top:2614px">Read More</div>
</section>

<section>
  <div class="photo office-warm" style="left:728px;top:2772px;width:359px;height:379px" role="img" aria-label="Photo: interview meeting in a modern office"></div>
  <div class="panel" style="left:113px;top:2788px;width:687px;height:348px">
    <h2 class="h2" style="left:51px;top:22px">Contact Us Today</h2>
    <p class="copy" style="left:54px;top:80px;width:490px">Please contact us today with your requirements , this can be care workers ,chef, welders, pipe fitters, caravan cabinet makers, medical workers. The UK list of required skills is extensive and the Philippines offersenglish speaking highly qualified hard working employees. Contact us today and make that first step to a highly motivated , quality skilled workforce.</p>
    <div class="btn light" style="left:54px;top:280px;height:40px">Read More</div>
  </div>
</section>

<section>
  <h2 class="h2" style="left:0;width:1200px;text-align:center;top:3208px">Working Together</h2>
  <p class="copy" style="left:0;width:1200px;text-align:center;top:3268px;font-size:15px">We recruit the finest talent available with our dedicated 200 strong team. Our centres are<br>highlighted in red dots on the map.</p>
  <div class="photo map" role="img" aria-label="Map of the Philippines with red dots marking recruitment centres"></div>
  <form class="panel form-panel">
    <h3>Contact Us Today</h3>
    <span class="field-label" style="top:60px">Name:</span><span class="field" style="top:87px"></span>
    <span class="field-label" style="top:150px">Phone</span><span class="field" style="top:177px"></span>
    <span class="field-label" style="top:237px">Email:</span><span class="field" style="top:264px"></span>
    <span class="field-label" style="top:320px">Message:</span><span class="field" style="top:347px"></span>
    <span class="send">Send Message</span>
  </form>
</section>

<footer class="site-footer">
  <div class="footer-title">Contact Details</div>
  <div class="contact-row">
    <span><svg width="14" height="14" viewBox="0 0 24 24" fill="#fff"><path d="M6.6 10.8a15 15 0 006.6 6.6l2.2-2.2c.3-.3.7-.4 1-.2 1.1.4 2.3.6 3.6.6.6 0 1 .4 1 1V20c0 .6-.4 1-1 1A17 17 0 013 4c0-.6.4-1 1-1h3.5c.6 0 1 .4 1 1 0 1.3.2 2.5.6 3.6.1.3 0 .7-.2 1z"/></svg>07700 900461</span>
    <span><svg width="15" height="12" viewBox="0 0 24 18" fill="#fff"><path d="M0 0h24v18H0z"/><path d="M0 0l12 9 12-9" stroke="#8b3129" stroke-width="2" fill="none"/></svg>sales@brackwellstaffing.example.com</span>
    <span><svg width="12" height="16" viewBox="0 0 12 16" fill="#fff"><path d="M6 0a6 6 0 016 6c0 4.5-6 10-6 10S0 10.5 0 6a6 6 0 016-6z"/><circle cx="6" cy="6" r="2.2" fill="#8b3129"/></svg>Orchard Row, Fenmoor FM4 2 United Kingdom</span>
  </div>
  <div class="footer-nav">Home &nbsp; | &nbsp; About &nbsp; | &nbsp; Services &nbsp; | &nbsp; Articles &nbsp; | &nbsp; Training &nbsp; | &nbsp; Contact us</div>
  <div class="social" aria-label="Social media links"><span></span><span></span><span></span><span></span></div>
  <div class="rule"></div>
  <div class="copyright">© 2023 All Rights Reserved | Brackwell Staffing Ltd</div>
</footer>

</body>
</html>
```